MMA fitness boot camp

We need a flyer that feels friendly and inviting to people who have never done fitness or training before. It also needs to look serious so it has the look of being a serious workout program.

We dont mind how it is set out as long as it conveys the message.

We do not want images of professional MMA fighters fighting. We like fitness training images that are relatable. eg- fit women punching or kicking a punching bag . If possible add men as well. We are aiming for men and women to do the boot camp.

The information for flyer is as below-

‘MMA Fitness Bootcamp’

Join us at Ironleaf Training Hub for our new Mixed Martial Arts Bootcamp. You will train for 4 weeks with the same fitness methods a professional fighter would use before a fight! You will get an intense and challenging workout whilst having fun. This isn’t your common boot camp held at the local park, this is unique and enjoyable!

During this 4 week period, you will be training twice a week early mornings in our Training facility.

Enjoy training in a supportive environment with an MMA fighter and qualified Master trainer pushing you every session so that you get the best out of yourself.

For more information email us at marcus@ironleaftraininghub.com.au or to book your spot with us.

or visit us at-
www.ironleaftraininghub.com

ALL FITNESS LEVELS WELCOME!

Level 1, 274 Quenby Rd. Smithfield.'

```html
<!DOCTYPE html>
<html lang="en">
<head>
<meta charset="utf-8">
<title>MMA Fitness Bootcamp</title>
<link rel="stylesheet" href="https://fonts.googleapis.com/css2?family=Open+Sans:wght@400;600&display=swap">
<style>
  :root {
    --yellow: #e6f03c;
    --green: #6fe041;
    --orange: #f1663e;
    --dark: #1b1617;
    --ink: #1d1d1d;
    --white: #ffffff;
  }
  * { margin: 0; padding: 0; box-sizing: border-box; }
  html, body { width: 849px; height: 1200px; overflow: hidden; }
  body { font-family: "Open Sans", Arial, sans-serif; background: var(--green); }
  .flyer { position: relative; width: 849px; height: 1200px; overflow: hidden; background: var(--green); }

  .header { position: absolute; left: 0; top: 0; width: 849px; height: 300px; background: var(--yellow); }
  .title { position: absolute; left: 120px; top: 72px; font-size: 46px; font-weight: 400; color: var(--ink); letter-spacing: 1px; }
  .clock-icon { position: absolute; left: 118px; top: 170px; width: 100px; height: 100px; }
  .address-band { position: absolute; left: 240px; top: 178px; width: 609px; height: 92px; background: var(--orange); }
  .address { position: absolute; left: 350px; top: 208px; font-size: 23px; color: var(--ink); }

  .intro { position: absolute; left: 120px; top: 322px; width: 620px; font-size: 23px; line-height: 31px; color: var(--white); text-align: justify; }
  .intro p { margin-bottom: 22px; }
  .intro p:last-child { margin-bottom: 0; text-align: left; }

  .welcome-band { position: absolute; left: 0; top: 790px; width: 580px; height: 80px; }
  .welcome { position: absolute; left: 120px; top: 816px; font-size: 23px; color: var(--white); }

  .footer { position: absolute; left: 0; top: 870px; width: 849px; height: 248px; background: var(--orange); }
  .mail-icon { position: absolute; left: 128px; top: 996px; width: 48px; height: 36px; }
  .email { position: absolute; left: 200px; top: 996px; font-size: 23px; color: var(--white); }
  .dot { position: absolute; top: 1076px; width: 24px; height: 24px; border-radius: 50%; background: var(--green); }
  .dot-1 { left: 108px; } .dot-2 { left: 413px; } .dot-3 { left: 712px; }

  .site-bar { position: absolute; left: 0; top: 1118px; width: 849px; height: 82px; background: var(--dark); }
  .website { position: absolute; left: 0; top: 1144px; width: 849px; text-align: center; font-size: 23px; color: var(--orange); }
</style>
</head>
<body>
<main class="flyer">
  <header class="header">
    <h1 class="title">MMA FITNESS BOOTCAMP</h1>
    <svg class="clock-icon" viewBox="0 0 100 100" aria-hidden="true">
      <circle cx="50" cy="50" r="46" fill="var(--green)" stroke="var(--orange)" stroke-width="6"/>
      <circle cx="50" cy="50" r="17" fill="none" stroke="var(--ink)" stroke-width="3"/>
      <path d="M50 40 V51 L56 56" fill="none" stroke="var(--ink)" stroke-width="3" stroke-linecap="round"/>
    </svg>
    <div class="address-band"></div>
    <p class="address">Level 1, 274 Quenby Rd. Smithfield.</p>
  </header>

  <section class="intro">
    <p>Join us at Ironleaf Training Hub for our new Mixed Martial Arts Bootcamp. You will train for 4 weeks with the same fitness methods a professional fighter would use before a fight! You will get an intense and challenging workout whilst having fun. This isn't your common boot camp held at the local park, this is unique and enjoyable!</p>
    <p>During this 4 week period, you will be training twice a week early mornings in our Training facility.</p>
    <p>Enjoy training in a supportive environment with an MMA fighter and qualified Master trainer pushing you every session so that you get the best out of yourself.</p>
    <p>For more information email us to book your spot with us.</p>
  </section>

  <svg class="welcome-band" viewBox="0 0 580 80" aria-hidden="true">
    <polygon points="0,14 500,14 580,0 580,80 0,80" fill="var(--orange)"/>
  </svg>
  <p class="welcome">ALL FITNESS LEVELS WELCOME!</p>

  <footer class="footer"></footer>
  <svg class="mail-icon" viewBox="0 0 48 36" aria-hidden="true">
    <rect x="1" y="1" width="46" height="34" fill="var(--dark)" transform="rotate(-12 24 18)"/>
    <path d="M4 6 L24 20 L44 2" fill="none" stroke="var(--orange)" stroke-width="2.5" transform="rotate(-12 24 18)"/>
  </svg>
  <p class="email">marcus@ironleaftraininghub.com.au</p>
  <span class="dot dot-1"></span>
  <span class="dot dot-2"></span>
  <span class="dot dot-3"></span>

  <div class="site-bar"></div>
  <p class="website">www.ironleaftraininghub.com</p>
</main>
</body>
</html>
```